Power Point - I have 5 webinars and each webinar has around 80-90 slides.

I have 5 webinars and each webinar has around 80-90 slides. This project is for the first of the five webinars; if the design is successful, the designer will be used for the subsequent 4 webinars, possibly for an increased fee.
The first of the 5 is a free webinar, showcasing what I can offer, as a service. The other 4 are on specific topics and the viewers will pay for them.
The target market for all the webinars are parents, but specifically, professional mothers who have children 10 years and under. ‘Professional’ is a loose term; they may have worked before they had children, they may work, part-time or full time, now, they may want to start a new career or project (set up a photography business, or community project).
I will provide the images and the copy for the designer. I would love the designer to use their creativity, so long as I get to look at the work and agree it as we go along. Since there are 5 webinars, I am happy for the whole thing to be working progress, as in we hone ‘the fit’ as we go along. The main thing I would like, over the 80-90 images is for each of them to represent the message I would like to portray. I want to be supportive of parents, offering them genuine methods for parenting.
The website and the logo are being designed now and will be incorporated into the following 4 webinars.
Actually, most of the slides, for this first (of 5 webinars) have been designed (around 35 have already been designed, leaving 50 more to be designed); the designer was unable to complete the rest. The file I have attached is a sample of what is required.

```html
<!DOCTYPE html>
<html lang="en">
<head>
<meta charset="utf-8">
<title>Calmer Family Life: The Webinars</title>
<link rel="stylesheet" href="https://fonts.googleapis.com/css2?family=Montserrat:wght@600;700;800&family=Playfair+Display:wght@400&display=swap">
<style>
  :root {
    --bar-black: #000000;
    --ink: #111111;
    --white: #ffffff;
    --sky-top: #cfe3ea;
    --sky-mid: #f3e4c8;
    --sky-warm: #f6b98a;
    --horizon-pink: #f29b9a;
    --sea: #8fa3b4;
    --sea-deep: #6f8598;
    --sand: #f2a27a;
    --sand-dark: #4a4240;
    --panel-tint: rgba(255, 240, 230, 0.38);
  }
  * { margin: 0; padding: 0; box-sizing: border-box; }
  html, body { width: 1200px; height: 900px; overflow: hidden; background: var(--white); }
  .slide {
    position: relative;
    width: 1200px;
    height: 900px;
    overflow: hidden;
    font-family: "Montserrat", Arial, sans-serif;
    color: var(--ink);
  }
  .top-bar {
    position: absolute;
    left: 0; top: 0;
    width: 1200px; height: 84px;
    background: var(--bar-black);
  }
  .presenter-name {
    position: absolute;
    left: 50px; top: 32px;
    font-weight: 700;
    font-size: 16px;
    letter-spacing: 0.06em;
    color: var(--white);
  }
  .beach-scene {
    position: absolute;
    left: 0; top: 84px;
    width: 1200px; height: 816px;
    background:
      linear-gradient(180deg,
        var(--sky-top) 0%,
        var(--sky-mid) 22%,
        var(--sky-warm) 38%,
        var(--horizon-pink) 47%,
        var(--sea) 51%,
        var(--sea-deep) 62%,
        var(--sand) 72%,
        #ee9a78 84%,
        var(--sand-dark) 100%);
  }
  .title-block {
    position: absolute;
    right: 50px; top: 100px;
    text-align: right;
    white-space: nowrap;
  }
  .series-title {
    font-family: "Playfair Display", Georgia, serif;
    font-weight: 400;
    font-size: 38px;
    line-height: 46px;
    color: var(--ink);
  }
  .series-subtitle {
    margin-top: 2px;
    font-family: "Montserrat", Arial, sans-serif;
    font-weight: 600;
    font-size: 37px;
    line-height: 44px;
    letter-spacing: 0.02em;
    color: var(--ink);
  }
  .schedule-panel {
    position: absolute;
    left: 534px; top: 346px;
    width: 614px; height: 415px;
    background: var(--panel-tint);
    padding: 6px 0 0 12px;
  }
  .session-title {
    font-weight: 800;
    font-size: 26px;
    line-height: 33.4px;
    white-space: nowrap;
  }
  .session-title .week { display: inline-block; width: 126px; }
  .session-date {
    padding-left: 120px;
    font-weight: 700;
    font-size: 23.5px;
    line-height: 33.4px;
    letter-spacing: 0.01em;
    white-space: nowrap;
  }
  sup { font-size: 0.6em; line-height: 0; vertical-align: 0.7em; }
</style>
</head>
<body>
<main class="slide">
  <div class="beach-scene" role="img" aria-label="Photograph of a beach at sunset with two people and a dog walking along the water's edge"></div>

  <header class="top-bar">
    <span class="presenter-name">MAREN ASHCOMBE</span>
  </header>

  <div class="title-block">
    <h1 class="series-title">CALMER FAMILY LIFE:&nbsp; LET’S FIND YOUR FOOTING</h1>
    <h2 class="series-subtitle">THE WEBINARS</h2>
  </div>

  <section class="schedule-panel">
    <div class="session">
      <p class="session-title"><span class="week">Week 1</span>Mealtime Matters</p>
      <p class="session-date">Held on Tuesday 11<sup>th</sup> April at 1pm</p>
      <p class="session-date">and Sunday 16<sup>th</sup> April at 8pm</p>
    </div>
    <div class="session">
      <p class="session-title"><span class="week">Week 2</span>Praise That Really Works</p>
      <p class="session-date">Held on Tuesday 18<sup>th</sup> April at 1pm</p>
      <p class="session-date">and Sunday 23<sup>rd</sup> April at 8pm</p>
    </div>
    <div class="session">
      <p class="session-title"><span class="week">Week 3</span>Balancing Device Time</p>
      <p class="session-date">Held on Tuesday 25<sup>th</sup> April at 1pm</p>
      <p class="session-date">and Sunday 30<sup>th</sup> April at 8pm</p>
    </div>
    <div class="session">
      <p class="session-title"><span class="week">Week 4</span>Learning Happily At Home</p>
      <p class="session-date">Held on Tuesday 2<sup>nd</sup> May at 1pm</p>
      <p class="session-date">and Sunday 7<sup>th</sup> May at 8pm</p>
    </div>
  </section>
</main>
</body>
</html>
```